Redesign of existing business card

I would like the "signage" attachment converted into a business card. This needs to be double sided aswell, keeping the phone number and names on the front, and the email + website on the back.

Second attachment is the current business card design.

Larger font for contact details is required.

Must keep to original color themes (electric blue, silver/grey etc)

Back of the card to have blue background with white writing.

Industry/Entity Type

Business

Contact Information for Business Card

Refer to existing design from attachments

Requirements
Must have
• Refer to existing design from attachments
Nice to have

```html
<!DOCTYPE html>
<html lang="en">
<head>
<meta charset="utf-8">
<title>Voltara Electric – Business Card, Front and Back</title>
<link rel="stylesheet" href="https://fonts.googleapis.com/css2?family=Exo+2:wght@300;400;600;700&display=swap">
<style>
  :root {
    --page-bg: #e6e4e0;
    --card-dark: #3b3c3f;
    --card-dark-deep: #2c2d30;
    --silver: #cfd1d4;
    --silver-light: #f4f5f6;
    --electric-blue: #1f4fe0;
    --electric-blue-deep: #1639b0;
    --text-light: #ffffff;
    --text-muted: #d9dadc;
  }
  * { box-sizing: border-box; margin: 0; padding: 0; }
  html, body {
    width: 1200px;
    height: 994px;
    overflow: hidden;
    background: var(--page-bg);
    font-family: "Exo 2", sans-serif;
  }
  .business-card {
    position: absolute;
    left: 220px;
    width: 760px;
    height: 434px;
    border-radius: 22px;
    overflow: hidden;
    box-shadow: 0 12px 34px rgba(0,0,0,0.22);
  }
  .card-front {
    top: 40px;
    background: linear-gradient(160deg, var(--card-dark) 0%, var(--card-dark-deep) 100%);
  }
  .card-back {
    top: 520px;
    background: linear-gradient(160deg, var(--electric-blue) 0%, var(--electric-blue-deep) 100%);
  }
  .card-art {
    position: absolute;
    inset: 0;
    width: 760px;
    height: 434px;
  }
  .brand-name {
    position: absolute;
    left: 44px;
    top: 42px;
    font-size: 34px;
    font-weight: 600;
    letter-spacing: 1.5px;
    text-transform: uppercase;
    color: var(--text-light);
    white-space: nowrap;
  }
  .person {
    position: absolute;
    left: 44px;
    top: 170px;
    color: var(--text-light);
  }
  .person-line {
    display: flex;
    align-items: baseline;
    gap: 12px;
  }
  .person-name { font-size: 32px; font-weight: 700; }
  .person-divider { font-size: 26px; font-weight: 300; }
  .person-role { font-size: 22px; font-weight: 300; color: var(--text-muted); }
  .person-licence {
    margin-top: 4px;
    font-size: 18px;
    font-weight: 300;
    letter-spacing: 1px;
    color: var(--text-muted);
  }
  .contact-list {
    position: absolute;
    left: 44px;
    list-style: none;
    color: var(--text-light);
  }
  .card-front .contact-list { top: 320px; }
  .card-back .contact-list { top: 290px; }
  .contact-item {
    display: flex;
    align-items: center;
    gap: 16px;
    height: 46px;
    font-size: 26px;
    font-weight: 400;
    white-space: nowrap;
  }
  .card-back .contact-item { font-size: 24px; }
  .contact-icon { width: 26px; height: 26px; flex: none; }
</style>
</head>
<body>
  <!-- Front -->
  <div class="business-card card-front">
    <svg class="card-art" viewBox="0 0 760 434" aria-hidden="true">
      <defs>
        <linearGradient id="light-panel" x1="0" y1="0" x2="1" y2="1">
          <stop offset="0" stop-color="#ffffff"/>
          <stop offset="1" stop-color="#e9eaec"/>
        </linearGradient>
        <clipPath id="light-clip">
          <path d="M430 0 H760 V434 H610 Q510 230 430 0 Z"/>
        </clipPath>
      </defs>
      <path d="M430 0 H760 V434 H610 Q510 230 430 0 Z" fill="url(#light-panel)"/>
      <g clip-path="url(#light-clip)">
        <circle cx="610" cy="195" r="150" fill="var(--silver)"/>
        <circle cx="610" cy="195" r="132" fill="var(--silver-light)"/>
      </g>
      <text x="625" y="205" text-anchor="middle" font-family="'Exo 2', sans-serif"
            font-size="30" font-weight="600" letter-spacing="1.5" fill="#1f4fe0">VOLTARA</text>
    </svg>

    <div class="brand-name">Voltara Electric</div>

    <div class="person">
      <div class="person-line">
        <span class="person-name">Daniel Reyes</span>
        <span class="person-divider">|</span>
        <span class="person-role">Director</span>
      </div>
      <div class="person-licence">EC10492</div>
    </div>

    <ul class="contact-list">
      <li class="contact-item">
        <svg class="contact-icon" viewBox="0 0 28 28" aria-hidden="true">
          <rect width="28" height="28" fill="var(--electric-blue)"/>
          <path d="M9 7 l3 0 l1.5 4 l-2 1.5 a9 9 0 0 0 4 4 l1.5 -2 l4 1.5 l0 3 a2 2 0 0 1 -2 2 a13 13 0 0 1 -12 -12 a2 2 0 0 1 2 -2 z" fill="#fff"/>
        </svg>
        <span>0400 555 123</span>
      </li>
    </ul>
  </div>

  <!-- Back -->
  <div class="business-card card-back">
    <svg class="card-art" viewBox="0 0 760 434" aria-hidden="true">
      <circle cx="610" cy="200" r="140" fill="var(--silver)"/>
      <circle cx="610" cy="200" r="122" fill="var(--silver-light)"/>
      <text x="610" y="210" text-anchor="middle" font-family="'Exo 2', sans-serif"
            font-size="30" font-weight="600" letter-spacing="1.5" fill="#1f4fe0">VOLTARA</text>
    </svg>

    <div class="brand-name">Voltara Electric</div>

    <ul class="contact-list">
      <li class="contact-item">
        <svg class="contact-icon" viewBox="0 0 28 28" aria-hidden="true">
          <rect width="28" height="28" fill="#fff"/>
          <rect x="6" y="8" width="16" height="12" fill="none" stroke="var(--electric-blue)" stroke-width="2"/>
          <path d="M6 8 L14 15 L22 8" fill="none" stroke="var(--electric-blue)" stroke-width="2"/>
        </svg>
        <span>daniel@voltaraelectric.com</span>
      </li>
      <li class="contact-item">
        <svg class="contact-icon" viewBox="0 0 28 28" aria-hidden="true">
          <rect width="28" height="28" fill="#fff"/>
          <circle cx="14" cy="14" r="8" fill="none" stroke="var(--electric-blue)" stroke-width="2"/>
          <path d="M6 14 H22 M14 6 Q9 14 14 22 M14 6 Q19 14 14 22" fill="none" stroke="var(--electric-blue)" stroke-width="1.6"/>
        </svg>
        <span>www.voltaraelectric.com.au</span>
      </li>
    </ul>
  </div>
</body>
</html>
```